I need a business card that is professional /minimalistic ( clean edges) to help develop my new business venture that is car valeting / detailing.

I would like to use a black background, white font,red car silhouette above the text.
Updates

have now added phone numbers thanks

Industry/Entity Type

Business

Contact Information for Business Card

Gleamcraft Studio,
Valeting & Detailing Specialist,
tel 01632 960418 mob 07700 900583, Dale Hextor, 7 Marlow Rise. West Fenby, Harlby. NR91 3XQ

```html
<!DOCTYPE html>
<html lang="en">
<head>
<meta charset="utf-8">
<title>Gleamcraft Studio — Business Card</title>
<link href="https://fonts.googleapis.com/css2?family=Open+Sans:wght@400;500;600&family=Roboto+Condensed:wght@700&display=swap" rel="stylesheet">
<style>
  :root {
    --page-bg: #b9b9b9;
    --card-dark: #262626;
    --band-dark: #333333;
    --stripe-light: #e6e6e6;
    --stripe-mid: #c9c9c9;
    --accent-green: #9dc60b;
    --text-white: #ffffff;
    --car-red: #e01010;
  }
  * { margin: 0; padding: 0; box-sizing: border-box; }
  html, body {
    width: 1200px; height: 900px; overflow: hidden;
    background: var(--page-bg);
  }
  .card {
    position: absolute; left: 233px; top: 209px;
    width: 777px; height: 467px;
    background: var(--card-dark);
    border: 1px solid #e8e8e8;
    box-shadow: 0 4px 10px rgba(0,0,0,0.35);
    overflow: hidden;
    font-family: "Open Sans", sans-serif;
    color: var(--text-white);
  }
  .holder {
    position: absolute; right: 74px; top: 66px; text-align: right;
  }
  .holder-name {
    font-size: 29px; font-weight: 400; letter-spacing: -1.5px; line-height: 1.2;
  }
  .holder-role {
    font-size: 16px; color: var(--accent-green); line-height: 1.1;
  }
  .brand {
    position: absolute; left: 39px; top: 160px;
  }
  .brand-name {
    font-family: "Roboto Condensed", sans-serif; font-weight: 700;
    font-size: 60px; line-height: 1; letter-spacing: -1px;
    text-transform: uppercase; color: var(--text-white);
  }
  .brand-tagline {
    margin-top: -2px; margin-left: 8px;
    font-size: 23px; letter-spacing: 1.2px;
  }
  .car-art {
    position: absolute; left: 572px; top: 218px; width: 185px; height: 84px;
  }
  .contact-band {
    position: absolute; left: 0; top: 279px; width: 100%; height: 110px;
    background: var(--band-dark);
  }
  .contact-item {
    position: absolute; top: 24px; display: flex; gap: 8px;
    font-size: 15px; font-weight: 500; line-height: 28px;
  }
  .contact-item svg { flex: none; margin-top: 6px; }
  .contact-address { left: 51px; }
  .contact-tel { left: 336px; }
  .contact-mob { left: 541px; }
  .stripe {
    position: absolute; left: 0; top: 389px; width: 100%; height: 18px;
    background: linear-gradient(var(--stripe-mid) 0 7px, var(--stripe-light) 7px 100%);
  }
  .green-band {
    position: absolute; left: 0; top: 407px; width: 100%; height: 60px;
    background: var(--accent-green);
  }
</style>
</head>
<body>
  <div class="card">
    <div class="holder">
      <div class="holder-name">YOUR NAME</div>
      <div class="holder-role">Position</div>
    </div>

    <div class="brand">
      <div class="brand-name">Gleamcraft Studio</div>
      <div class="brand-tagline">Valeting &amp; Detailing Specialist</div>
    </div>

    <svg class="car-art" role="img" aria-label="Red line drawing of a sports car" viewBox="0 0 185 84">
      <defs>
        <radialGradient id="carGlow" cx="50%" cy="55%" r="55%">
          <stop offset="0" stop-color="#e01010" stop-opacity="0.45"/>
          <stop offset="1" stop-color="#e01010" stop-opacity="0"/>
        </radialGradient>
      </defs>
      <rect width="185" height="84" fill="url(#carGlow)"/>
    </svg>

    <div class="contact-band">
      <div class="contact-item contact-address">
        <svg width="13" height="18" viewBox="0 0 13 18" aria-hidden="true">
          <path d="M6.5 0A6.5 6.5 0 0 0 0 6.5C0 11 6.5 18 6.5 18S13 11 13 6.5A6.5 6.5 0 0 0 6.5 0Zm0 9.3a2.8 2.8 0 1 1 0-5.6 2.8 2.8 0 0 1 0 5.6Z" fill="var(--accent-green)"/>
        </svg>
        <div>Dale Hextor, 7 Marlow Rise.<br>West Fenby, Harlby. NR91 3XQ</div>
      </div>
      <div class="contact-item contact-tel">
        <svg width="10" height="16" viewBox="0 0 10 16" aria-hidden="true">
          <path d="M2 1h3l1 4-2 1c.5 2 1.5 3.5 3 4.5l1.5-1.5 2 2.5-2 3C4 13.5 1 9 1 4Z" fill="var(--accent-green)" transform="translate(-1 0)"/>
        </svg>
        <div>&nbsp;+(01632) 960-418</div>
      </div>
      <div class="contact-item contact-mob">
        <svg width="10" height="17" viewBox="0 0 10 17" aria-hidden="true">
          <rect x="0.5" y="0.5" width="9" height="16" rx="1.5" fill="var(--accent-green)"/>
          <rect x="2" y="2.5" width="6" height="5" fill="var(--band-dark)"/>
          <g fill="var(--band-dark)">
            <rect x="2" y="9" width="1.5" height="1.2"/><rect x="4.25" y="9" width="1.5" height="1.2"/><rect x="6.5" y="9" width="1.5" height="1.2"/>
            <rect x="2" y="11" width="1.5" height="1.2"/><rect x="4.25" y="11" width="1.5" height="1.2"/><rect x="6.5" y="11" width="1.5" height="1.2"/>
            <rect x="2" y="13" width="1.5" height="1.2"/><rect x="4.25" y="13" width="1.5" height="1.2"/><rect x="6.5" y="13" width="1.5" height="1.2"/>
          </g>
        </svg>
        <div>+(07700) 900-583</div>
      </div>
    </div>

    <div class="stripe"></div>
    <div class="green-band"></div>
  </div>
</body>
</html>
```